PELDRAX Business Cards

We require a business card for our company that provides IT consulting services. We already have a logo that needs to be used on the card. We want a clean professional looking design that incorporates our colours. Our main focus is providing managed services to business, which involves us looking after all of their IT requirements including managing servers/networks, projects, and procurement.

Industry/Entity Type

Information Technology

Requirements
Must have
• our logo, contact information, name, title, phone numbers

```html
<!DOCTYPE html>
<html lang="en">
<head>
<meta charset="utf-8">
<title>PELDRAX Business Cards</title>
<link rel="stylesheet" href="https://fonts.googleapis.com/css2?family=Roboto:wght@400;500&display=swap">
<style>
  :root {
    --backdrop: #2a2a2a;
    --paper: #f4f4f2;
    --brand-blue: #0e93d1;
    --ink: #2b2b2b;
    --white: #ffffff;
  }
  * { margin: 0; padding: 0; box-sizing: border-box; }
  html, body { width: 1200px; height: 1200px; overflow: hidden; }
  body {
    background: var(--backdrop);
    font-family: "Roboto", Arial, sans-serif;
    position: relative;
  }
  .card {
    position: absolute;
    top: 271px;
    width: 384px;
    height: 673px;
  }
  .card-front { left: 204px; background: var(--paper); color: var(--ink); }
  .card-back { left: 611px; background: var(--brand-blue); color: var(--white); }

  .front-wordmark {
    position: absolute;
    left: 26px;
    top: 108px;
    font-size: 46px;
    font-weight: 500;
    letter-spacing: 2px;
    color: var(--brand-blue);
  }
  .contact-block { position: absolute; left: 23px; top: 420px; }
  .person-name {
    font-size: 29px;
    font-weight: 500;
    color: var(--brand-blue);
    line-height: 1.1;
  }
  .person-title { font-size: 14px; margin-top: 4px; }
  .address { font-size: 15px; line-height: 20px; margin-top: 37px; }
  .contact-list { list-style: none; margin-top: 24px; }
  .contact-list li {
    display: flex;
    align-items: center;
    font-size: 15px;
    height: 22px;
  }
  .contact-list svg { width: 15px; height: 15px; margin-right: 11px; fill: var(--brand-blue); }

  .back-mark {
    position: absolute;
    left: 50%;
    top: 170px;
    width: 92px;
    height: 92px;
    margin-left: -46px;
    border-radius: 50%;
    background: var(--white);
  }
  .back-wordmark {
    position: absolute;
    left: 0;
    right: 0;
    top: 300px;
    text-align: center;
    font-size: 64px;
    font-weight: 500;
    letter-spacing: 3px;
  }
  .back-url {
    position: absolute;
    left: 193px;
    top: 516px;
    transform: translate(-50%, -50%) rotate(-90deg);
    font-size: 14px;
    letter-spacing: 1.5px;
    white-space: nowrap;
  }
  .back-rule {
    position: absolute;
    left: 192px;
    top: 606px;
    width: 1.5px;
    height: 67px;
    background: var(--white);
  }
</style>
</head>
<body>
  <section class="card card-front">
    <div class="front-wordmark">PELDRAX</div>
    <div class="contact-block">
      <div class="person-name">Mara Ellison</div>
      <div class="person-title">Founder &amp; CEO</div>
      <p class="address">48, Harwick Lane, Unit# B<br>Bristol, UK 7QF219</p>
      <ul class="contact-list">
        <li>
          <svg viewBox="0 0 24 24" aria-hidden="true"><path d="M6.6 10.8a15.1 15.1 0 0 0 6.6 6.6l2.2-2.2a1 1 0 0 1 1-.25 11.4 11.4 0 0 0 3.6.57 1 1 0 0 1 1 1V20a1 1 0 0 1-1 1A17 17 0 0 1 3 4a1 1 0 0 1 1-1h3.5a1 1 0 0 1 1 1c0 1.25.2 2.45.57 3.57a1 1 0 0 1-.25 1z"/></svg>
          020 555 0184
        </li>
        <li>
          <svg viewBox="0 0 24 24" aria-hidden="true"><path d="M2 5h20v2l-10 6L2 7z"/><path d="M2 9l10 6 10-6v10H2z"/></svg>
          info@peldrax.com
        </li>
        <li>
          <svg viewBox="0 0 24 24" aria-hidden="true"><path d="M12 2a10 10 0 1 0 0 20 10 10 0 0 0 0-20zm7.9 9h-3.4a15 15 0 0 0-1.3-6A8 8 0 0 1 19.9 11zM12 4c1 1.3 2.2 3.8 2.5 7h-5C9.8 7.8 11 5.3 12 4zM8.8 5a15 15 0 0 0-1.3 6H4.1A8 8 0 0 1 8.8 5zM4.1 13h3.4a15 15 0 0 0 1.3 6A8 8 0 0 1 4.1 13zM12 20c-1-1.3-2.2-3.8-2.5-7h5c-.3 3.2-1.5 5.7-2.5 7zm3.2-1a15 15 0 0 0 1.3-6h3.4a8 8 0 0 1-4.7 6z"/></svg>
          www.peldrax.com
        </li>
      </ul>
    </div>
  </section>

  <section class="card card-back">
    <div class="back-mark"></div>
    <div class="back-wordmark">PELDRAX</div>
    <div class="back-url">www.peldrax.com</div>
    <div class="back-rule"></div>
  </section>
</body>
</html>
```